Visitenkarten für eine Hypnose-Praxis
Ich bin sehr zufrieden mit der professionellen Arbeitsweise von KOR7342. Es war immer ein netter Kontakt und meine Wünsche wurden schnell umgesetzt. Alle Vorschläge waren sehr kreativ und und so viel es mir leicht, eine schnelle Entscheidung zu treffen.
Zielgruppe
Wir sind eine Hypnose-Praxis und richten unser Angebot an Privatpersonen unterschiedlichen Alters, die therapeutische Unterstützung suchen.
Aufgabenstellung
Eher schlichtes und modernes Design

```html
<!DOCTYPE html>
<html lang="de">
<head>
<meta charset="utf-8">
<title>Visitenkarten – sanftwelt Hypnose-Praxis</title>
<link href="https://fonts.googleapis.com/css2?family=Lato:ital,wght@0,400;0,700;1,700&display=swap" rel="stylesheet">
<style>
  :root {
    --page-bg: #f5f5f5;
    --card-bg: #ffffff;
    --accent-blue: #6ab2cf;
    --ink: #1a1a1a;
  }
  html, body {
    margin: 0;
    padding: 0;
    width: 1200px;
    height: 848px;
    overflow: hidden;
    background: var(--page-bg);
    font-family: "Lato", Arial, sans-serif;
    color: var(--ink);
  }
  .stage {
    position: relative;
    width: 1200px;
    height: 848px;
  }
  .card {
    position: absolute;
    width: 360px;
    height: 211px;
    background: var(--card-bg);
    overflow: hidden;
    box-shadow: 0 6px 10px rgba(0,0,0,0.08);
  }
  .card--front { left: 175px; top: 345px; }
  .card--back  { left: 608px; top: 345px; }
  .card__band {
    position: absolute;
    inset: 0;
    width: 100%;
    height: 100%;
  }
  .brand {
    position: absolute;
    left: 28px;
    top: 118px;
    display: flex;
    align-items: center;
    gap: 10px;
  }
  .brand__square {
    width: 22px;
    height: 22px;
    border-radius: 4px;
    background: var(--accent-blue);
  }
  .brand__name {
    font-size: 38px;
    font-weight: 700;
    letter-spacing: -0.5px;
    line-height: 1;
    color: var(--ink);
  }
  .contact {
    position: absolute;
    left: 28px;
    top: 19px;
    font-size: 9.6px;
    line-height: 1.42;
  }
  .contact__mark {
    width: 12px;
    height: 12px;
    border-radius: 3px;
    background: var(--accent-blue);
    margin-bottom: 7px;
  }
  .contact__name {
    font-size: 12.5px;
    font-weight: 700;
    font-style: italic;
    margin: 0 0 3px 36px;
  }
  .contact__block {
    margin: 0 0 6px 36px;
  }
  .contact__titles { font-weight: 700; }
  .contact__row { display: flex; }
  .contact__label { width: 60px; }
</style>
</head>
<body>
<main class="stage">
  <section class="card card--front" aria-label="Vorderseite">
    <svg class="card__band" viewBox="0 0 360 211" preserveAspectRatio="none" aria-hidden="true">
      <polygon fill="var(--accent-blue)" points="312,0 360,0 360,211 286,211"/>
    </svg>
    <div class="brand">
      <span class="brand__square"></span>
      <span class="brand__name">sanftwelt</span>
    </div>
  </section>

  <section class="card card--back" aria-label="Rückseite">
    <svg class="card__band" viewBox="0 0 360 211" preserveAspectRatio="none" aria-hidden="true">
      <polygon fill="var(--accent-blue)" points="312,0 360,0 360,211 286,211"/>
    </svg>
    <div class="contact">
      <div class="contact__mark"></div>
      <p class="contact__name">Lena Hartwig</p>
      <div class="contact__block contact__titles">
        Diplom-Psychologin<br>
        Heilpraktikerin für Psychotherapie<br>
        mit Spezialisierung Hypnose-Therapie
      </div>
      <div class="contact__block">
        Lindenweg 14<br>
        10115 Berlin
      </div>
      <div class="contact__block">
        <div class="contact__row"><span class="contact__label">Telefon</span><span>030 / 51 28 44 70</span></div>
        <div class="contact__row"><span class="contact__label">24-Std-AB</span><span>030 / 51 28 44 79</span></div>
      </div>
      <div class="contact__block">
        info@sanftwelt-hypnose.de<br>
        www.sanftwelt-hypnose.de
      </div>
    </div>
  </section>
</main>
</body>
</html>
```